PulseCrest VK - 8 oz Bottle Label Design

I really like the Example label I uploaded. However it need to be cleaned up...

We are designing a premium supplement label for Pulse Crest VK, a clinically inspired herbal cardiovascular support formula. This is a serious, professional product — not flashy, not gimmicky. The brand should feel medical-grade, authoritative, clean, and trustworthy. Think pharmaceutical confidence meets modern nutraceutical branding. The primary brand color is deep red (#D40000), used in the logo and subtle accent elements. The bottle is white with a black cap. The design must look powerful but disciplined — strong typography, clean spacing, no clutter, no cartoon graphics, no flames or exaggerated imagery.

The label size is 3 inches tall by 8 inches wide (wrap layout). It must include the Pulse Crest VK logo prominently, the three key herbs (Terminalia Arjuna, Hawthorn Berry, Astragalus), “60 Vegetable Capsules,” Suggested Use, Caution statements, FDA disclaimer, distributor information (MorvenWellco.example – Bakersfield, California), and a properly formatted Supplement Facts panel. The layout must balance all regulatory information while maintaining a premium clinical aesthetic. We want this to look like a nationally distributed, high-end heart support formula — clean, structured, and high-definition, print-ready with transparent background.
Resolution: 300 DPI
Dimensions: 1800 × 750 pixels
Background: Fully transparent

SIDE PANEL – SUPPLEMENT FACTS (FDA Style Layout)
SUPPLEMENT FACTS
Serving Size: 2 Capsules
Servings Per Container: 30
Amount Per Serving:
Terminalia Arjuna (Bark Extract) — 700 mg
Hawthorn Berry Extract (Crataegus spp.) — 400 mg
Astragalus Root Extract (Astragalus membranaceus) — 400 mg
Total Herbal Complex — 1,500 mg
Other Ingredients:
Vegetable Capsule.

PULSE CREST VK
(Logo exactly as uploaded)
Below Logo (Small Caps, Clean Font):
Advanced Cardiovascular Support
Center Highlight (Bold, Clinical):
1500 mg Herbal Complex
Per Serving (2 Capsules)
Thin black divider line
Terminalia Arjuna • Hawthorn Berry • Astragalus
Thin divider line
Supports Heart Muscle Strength
Healthy Circulation & Cardiac Function*
Bottom Section:
60 Capsules
30 Day Supply
Dietary Supplement
Add a subtle red horizontal bar at bottom for visual anchor.

Primary Red: #D40000
Bottle: White
Cap: Black
Finish: Matte label (recommended)

SUPPLEMENT FACTS
Serving Size: 2 Capsules
Amount Per Serving:

Other Ingredients:
Vegetable Capsule.

Suggested Use:
Take 1 capsule in the morning and 1 capsule in the evening with water, or as directed by your healthcare professional.

Warning:
Consult your physician before use if pregnant, nursing, taking medication, or under medical supervision.

These statements have not been evaluated by the Food and Drug Administration. This product is not intended to diagnose, treat, cure, or prevent any disease.

Target Market(s)

55+ Male and Females

Industry/Entity Type

Health Supplements

Requirements
Must have
• Barcode. Made in USA flag.
Should not have
• GMP Button.

```html
<!DOCTYPE html>
<html lang="en">
<head>
<meta charset="utf-8">
<title>Pulse Crest VK – Bottle Label</title>
<link href="https://fonts.googleapis.com/css2?family=Oswald:wght@400;500;700&family=Roboto+Condensed:wght@400;700&family=Inter:wght@400;600;700&display=swap" rel="stylesheet">
<style>
  :root {
    --brand-red: #D40000;
    --ink: #1c1c1c;
    --ink-soft: #4a4a4a;
    --rule: #9a9a9a;
    --label-bg: #ffffff;
    --stage: #d6d6d6;
    --flag-blue: #2b3f8f;
  }
  * { box-sizing: border-box; margin: 0; padding: 0; }
  html, body { width: 876px; height: 1200px; overflow: hidden; }
  body { background: var(--stage); position: relative; font-family: "Inter", sans-serif; color: var(--ink); }

  .label {
    position: absolute; left: 20px; top: 448px; width: 836px; height: 304px;
    background: var(--label-bg);
  }
  .label__base-bar { position: absolute; left: 0; right: 0; bottom: 0; height: 6px; background: var(--brand-red); }

  /* Left panel */
  .info-panel { position: absolute; left: 16px; top: 20px; width: 176px; font-size: 6.4px; line-height: 1.45; color: var(--ink-soft); }
  .info-panel h4 { font-family: "Roboto Condensed", sans-serif; font-size: 7px; font-weight: 700; color: var(--ink); letter-spacing: .3px; }
  .info-panel p { margin-bottom: 9px; }
  .info-panel ul { list-style: none; margin-bottom: 10px; }
  .info-panel li::before { content: "• "; color: var(--brand-red); }
  .info-panel .distributor { margin-top: 6px; }
  .info-panel .handle { margin-top: 34px; margin-bottom: 2px; font-size: 6px; letter-spacing: .4px; }
  .info-panel .batch { font-weight: 700; color: var(--ink); }

  /* Front panel */
  .front-panel { position: absolute; left: 210px; top: 16px; width: 380px; text-align: center; }
  .brand { display: flex; align-items: center; justify-content: center; gap: 10px; }
  .brand__name { font-family: "Oswald", sans-serif; font-weight: 700; color: var(--brand-red); font-size: 42px; line-height: .95; text-align: left; letter-spacing: 1px; }
  .brand__dot { width: 30px; height: 30px; border-radius: 50%; background: var(--brand-red); }
  .tagline { margin-top: 8px; font-family: "Oswald", sans-serif; font-weight: 500; font-size: 14px; letter-spacing: 1.2px; color: #3a3a3a; border-bottom: 1px solid var(--rule); padding-bottom: 5px; }
  .highlight { display: flex; align-items: center; justify-content: center; gap: 12px; margin-top: 8px; }
  .highlight__item { display: flex; align-items: center; gap: 4px; }
  .highlight__num { font-family: "Oswald", sans-serif; font-weight: 700; font-size: 17px; color: var(--ink); }
  .highlight__num--red { color: var(--brand-red); font-size: 26px; }
  .highlight__cap { font-family: "Roboto Condensed", sans-serif; font-size: 7px; line-height: 1.1; text-align: left; text-transform: uppercase; color: var(--ink-soft); }
  .highlight__sep { width: 1px; height: 28px; background: var(--rule); }
  .herbs { font-family: "Roboto Condensed", sans-serif; font-weight: 700; font-size: 10px; line-height: 1.3; text-align: left; }
  .benefits { margin-top: 8px; border-top: 1px solid var(--ink); padding-top: 6px; font-family: "Roboto Condensed", sans-serif; font-size: 12px; line-height: 1.3; color: var(--ink); }
  .front-footer { margin-top: 12px; display: flex; align-items: center; justify-content: space-between; padding: 0 28px; }
  .count { font-family: "Oswald", sans-serif; font-weight: 700; font-size: 20px; line-height: 1.05; text-align: center; }
  .count small { display: block; font-size: 8px; line-height: 1.2; font-weight: 500; letter-spacing: 1px; }
  .supplement-pill { background: var(--brand-red); color: #fff; font-family: "Oswald", sans-serif; font-weight: 500; font-size: 10px; letter-spacing: 1px; padding: 3px 12px; }

  /* Right panel */
  .facts-panel { position: absolute; left: 612px; top: 16px; width: 206px; }
  .facts { border: 1.5px solid var(--ink); padding: 4px 6px; font-size: 6.4px; }
  .facts__title { font-family: "Oswald", sans-serif; font-weight: 700; font-size: 16px; line-height: 1; border-bottom: 1px solid var(--ink); padding-bottom: 3px; }
  .facts__row { display: flex; justify-content: space-between; gap: 6px; padding: 2px 0; border-bottom: 0.5px solid var(--ink); }
  .facts__row--thick { border-bottom: 3px solid var(--ink); }
  .facts__row b { font-weight: 700; }
  .facts__other { padding-top: 3px; }
  .disclaimer { margin-top: 6px; font-size: 5.6px; line-height: 1.4; color: var(--ink-soft); }
  .badges { margin-top: 8px; display: flex; gap: 8px; }
  .badge { width: 26px; height: 26px; border-radius: 50%; background: var(--flag-blue); }
  .badge--red { background: var(--brand-red); }
</style>
</head>
<body>
  <section class="label">
    <div class="info-panel">
      <h4>WARNINGS:</h4>
      <p>Consult your physician before use if pregnant, nursing, taking medication or under medical supervision.</p>
      <h4>SUGGESTED USE:</h4>
      <p>Take 1 capsule in the morning and 1 capsule in the evening with water, or as directed by your healthcare professional.</p>
      <ul>
        <li>Store in a cool, dry place away from sunlight.</li>
        <li>Do not exceed suggested use.</li>
        <li>Keep out of reach of children.</li>
      </ul>
      <p class="distributor">Distributed by: MorvenWellco.example<br>Bakersfield, California</p>
      <p class="handle">@PULSECRESTVK</p>
      <p class="batch">BATCH: &nbsp;&nbsp;&nbsp;&nbsp;&nbsp;&nbsp; EXP:</p>
    </div>

    <div class="front-panel">
      <div class="brand">
        <div class="brand__name">PULSE<br>CREST VK</div>
        <span class="brand__dot"></span>
      </div>
      <div class="tagline">ADVANCED CARDIOVASCULAR SUPPORT</div>
      <div class="highlight">
        <div class="highlight__item"><span class="highlight__num">1500mg</span><span class="highlight__cap">Herbal<br>Complex</span></div>
        <span class="highlight__sep"></span>
        <div class="highlight__item"><span class="highlight__cap">Per<br>Serving</span><span class="highlight__num highlight__num--red">2</span><span class="highlight__cap">Capsules</span></div>
        <span class="highlight__sep"></span>
        <div class="herbs">Terminalia Arjuna<br>Hawthorn Berry<br>Astragalus</div>
      </div>
      <div class="benefits">Support Heart Muscle Strength<br>Healthy Circulation &amp; Cardiac Function*</div>
      <div class="front-footer">
        <div class="count">60<small>CAPSULES</small></div>
        <span class="supplement-pill">DIETARY SUPPLEMENT</span>
        <div class="count">30<small>DAY SUPPLY</small></div>
      </div>
    </div>

    <div class="facts-panel">
      <div class="facts">
        <div class="facts__title">Supplement Facts</div>
        <div class="facts__row"><span>Serving Size: 2 Capsules</span></div>
        <div class="facts__row facts__row--thick"><span>Servings Per Container: 30</span></div>
        <div class="facts__row"><b>Amount Per Serving</b><b>% DV</b></div>
        <div class="facts__row"><span>Terminalia Arjuna (Bark Extract)</span><span>700 mg</span></div>
        <div class="facts__row"><span>Hawthorn Berry Extract (Crataegus spp.)</span><span>400 mg</span></div>
        <div class="facts__row"><span>Astragalus Root Extract (A. membranaceus)</span><span>400 mg</span></div>
        <div class="facts__row facts__row--thick"><b>Total Herbal Complex</b><b>1,500 mg</b></div>
        <div class="facts__other"><b>Other Ingredients:</b> Vegetable Capsule.</div>
      </div>
      <p class="disclaimer">*These statements have not been evaluated by the Food and Drug Administration. This product is not intended to diagnose, treat, cure, or prevent any disease.</p>
      <div class="badges">
        <span class="badge"></span>
        <span class="badge badge--red"></span>
      </div>
    </div>

    <div class="label__base-bar"></div>
  </section>
</body>
</html>
```